New Business Card for Casual Beachfront Cafe

Quirky Beachfront Cafe at Moana, South Australia needs a DOUBLE SIDED business card to print on PrintHarbor.

Target Market(s)

Business Cards sit on the counter for Guests to take with them. Please view our website www.saltreefcafe.com.au to get a feel for the Cafe. You may also view our Instagram at @saltreefcafe

Industry/Entity Type

Cafe / Restaurant

Contact Information for Business Card

Information equivalent to: Breakfast, Lunch, Dinner, Coffee, Takeaway / 117 Parade Coralby SA 5999 / Menu & Opening Hours: www.saltreefcafe.com.au / ph (08) 8461 9273

Requirements
Must have
• Information equivalent to: Breakfast, Lunch, Dinner, Coffee, Takeaway / 117 Parade Coralby SA 5999 / Menu & Opening Hours: www.saltreefcafe.com.au / ph (08) 8461 9273
Nice to have
• Potentially some of our trademark colours (Cafe can be searched via Seekly)
Should not have
• Must NOT have image of the building. May have the logo provided on one side but not necessarily, depending on how you wish to design the card

```html
<!DOCTYPE html>
<html lang="en">
<head>
<meta charset="utf-8">
<title>Salt Reef Cafe – Business Card</title>
<link rel="stylesheet" href="https://fonts.googleapis.com/css2?family=Jost:wght@400;500;600;700&display=swap">
<style>
  :root {
    --navy: #13487e;
    --lemon: #f2ea0b;
    --white: #ffffff;
    --backdrop: #f1f1f1;
    --card-w: 800px;
    --card-h: 457px;
    --radius: 52px;
    --strip: 82px;
  }
  * { box-sizing: border-box; margin: 0; padding: 0; }
  html, body {
    width: 1200px; height: 1200px; overflow: hidden;
    background: var(--backdrop);
    font-family: "Jost", sans-serif;
  }
  .card {
    position: absolute; left: 202px;
    width: var(--card-w); height: var(--card-h);
    border-radius: var(--radius); overflow: hidden;
  }
  .card--front { top: 102px; background: var(--navy); }
  .card--back  { top: 643px; background: var(--lemon); }

  .side-strip {
    position: absolute; left: 0; top: 0; bottom: 0; width: var(--strip);
  }
  .card--front .side-strip { background: var(--lemon); color: var(--navy); }
  .card--back  .side-strip { background: var(--navy); color: var(--lemon); }

  .side-strip__url {
    position: absolute; left: 41px; top: 199px;
    transform: translate(-50%, -50%) rotate(-90deg);
    white-space: nowrap; font-size: 22px; font-weight: 400; letter-spacing: 0.3px;
  }
  .side-strip__globe {
    position: absolute; left: 22px; width: 38px; height: 38px;
  }
  .card--front .side-strip__globe { top: 347px; }
  .card--back  .side-strip__globe { top: 345px; }

  .accent-rule {
    position: absolute; left: var(--strip); top: 88px;
    width: 279px; height: 5px; background: var(--lemon);
  }
  .identity { position: absolute; left: 412px; top: 52px; }
  .identity__name {
    color: var(--lemon); font-size: 44px; font-weight: 600; line-height: 1; letter-spacing: 0.5px;
  }
  .identity__role {
    color: var(--white); font-size: 21px; font-weight: 400; margin-top: 4px; letter-spacing: 0.2px;
  }

  .contact-list { position: absolute; left: 112px; top: 269px; list-style: none; }
  .contact-list__item {
    display: flex; align-items: center; height: 40px; margin-bottom: 13px;
    color: var(--white); font-size: 23px; font-weight: 400; letter-spacing: 0.5px;
    white-space: nowrap;
  }
  .contact-list__icon { width: 40px; height: 40px; flex: none; margin-right: 13px; }

  .wordmark {
    position: absolute; display: flex; flex-direction: column;
    align-items: center; justify-content: center; text-align: center;
    font-weight: 700; line-height: 0.95; letter-spacing: 1px;
  }
  .wordmark--front {
    left: 497px; top: 272px; width: 269px; height: 140px;
    color: var(--lemon); font-size: 44px;
  }
  .wordmark--back {
    left: 249px; top: 107px; width: 343px; height: 178px;
    color: var(--navy); font-size: 58px;
  }
  .edge-tab {
    position: absolute; left: 771px; top: 295px; width: 29px; height: 94px;
    background: var(--lemon);
  }
  .services {
    position: absolute; left: 170px; width: 482px; top: 309px;
    text-align: center; white-space: nowrap;
    color: var(--navy); font-size: 23px; font-weight: 400; letter-spacing: 0.5px;
  }
</style>
</head>
<body>

<section class="card card--front" aria-label="Card front">
  <div class="side-strip">
    <span class="side-strip__url">www.saltreefcafe.com.au</span>
    <svg class="side-strip__globe" viewBox="0 0 40 40" aria-hidden="true">
      <circle cx="20" cy="20" r="20" fill="var(--navy)"/>
      <g fill="none" stroke="var(--lemon)" stroke-width="1.8">
        <circle cx="20" cy="20" r="11"/>
        <ellipse cx="20" cy="20" rx="5" ry="11"/>
        <line x1="9" y1="20" x2="31" y2="20"/>
        <line x1="20" y1="9" x2="20" y2="31"/>
        <line x1="11" y1="14.5" x2="29" y2="14.5"/>
        <line x1="11" y1="25.5" x2="29" y2="25.5"/>
      </g>
    </svg>
  </div>

  <div class="accent-rule"></div>

  <div class="identity">
    <h1 class="identity__name">SALT REEF CAFE</h1>
    <p class="identity__role">FOUNDER/CEO</p>
  </div>

  <ul class="contact-list">
    <li class="contact-list__item">
      <svg class="contact-list__icon" viewBox="0 0 40 40" aria-hidden="true">
        <circle cx="20" cy="20" r="20" fill="var(--lemon)"/>
        <path d="M14 10.5c1.2-.8 2.3-.6 3 .5l2.2 3.4c.6 1 .4 2-.5 2.7l-1.4 1c.9 2.3 2.4 4.4 4.3 6l1.5-.9c1-.6 2-.4 2.6.5l2.2 3.2c.7 1 .5 2.1-.6 2.8-2 1.3-4.3 1.2-6.5-.4-3.8-2.8-6.6-6.7-7.9-11.2-.7-2.7-.4-5.8 1.1-7.6z" fill="var(--navy)"/>
      </svg>
      ph (08) 8461 9273
    </li>
    <li class="contact-list__item">
      <svg class="contact-list__icon" viewBox="0 0 40 40" aria-hidden="true">
        <circle cx="20" cy="20" r="20" fill="var(--lemon)"/>
        <rect x="9.5" y="13" width="21" height="14" fill="none" stroke="var(--navy)" stroke-width="2"/>
        <path d="M9.5 13l10.5 8 10.5-8M9.5 27l8-6.5M30.5 27l-8-6.5" fill="none" stroke="var(--navy)" stroke-width="1.8"/>
      </svg>
      saltreefcafe@info.com.au
    </li>
    <li class="contact-list__item">
      <svg class="contact-list__icon" viewBox="0 0 40 40" aria-hidden="true">
        <circle cx="20" cy="20" r="20" fill="var(--lemon)"/>
        <path d="M20 31s-7.5-8.6-7.5-13.8a7.5 7.5 0 0 1 15 0C27.5 22.4 20 31 20 31z" fill="var(--navy)"/>
        <circle cx="20" cy="17.2" r="3" fill="var(--lemon)"/>
      </svg>
      117 Parade Coralby SA 5999
    </li>
  </ul>

  <p class="wordmark wordmark--front">SALT REEF<br>CAFE</p>
  <div class="edge-tab"></div>
</section>

<section class="card card--back" aria-label="Card back">
  <div class="side-strip">
    <span class="side-strip__url">www.saltreefcafe.com.au</span>
    <svg class="side-strip__globe" viewBox="0 0 40 40" aria-hidden="true">
      <circle cx="20" cy="20" r="20" fill="var(--lemon)"/>
      <g fill="none" stroke="var(--navy)" stroke-width="1.8">
        <circle cx="20" cy="20" r="11"/>
        <ellipse cx="20" cy="20" rx="5" ry="11"/>
        <line x1="9" y1="20" x2="31" y2="20"/>
        <line x1="20" y1="9" x2="20" y2="31"/>
        <line x1="11" y1="14.5" x2="29" y2="14.5"/>
        <line x1="11" y1="25.5" x2="29" y2="25.5"/>
      </g>
    </svg>
  </div>

  <p class="wordmark wordmark--back">SALT REEF<br>CAFE</p>
  <p class="services">Breakfast, Lunch, Dinner, Coffee, Takeaway</p>
</section>

</body>
</html>
```